Garden building leaflet A4 tri fold

We need an A4 tri fold (printed both sides) flyer design for a local business based in East Hampshire (UK) called Corrick Yard Buildings.We offer a bespoke garden building service from design, construction, installation and maintenance.Typical use is for home office, garden studio, playrooms, garage workshops, therapy rooms and extra living accommodation. Including connection to all services as required.The final design should stress that this is a local business that has been serving the East Hampshire community for almost 20 years. Over this time Corrick's has built a reputation for quality construction with customer satisfaction the overriding driving force.Over the last 20 years we've seen a huge increase in people working from home at least one day per week and a shift back to family focused lifestyles. Even large multi national companies are promoting home working as it has been shown by recent studies home workers are more productive than solely office based employees. Corrick Yard Buildings is a greener way of working, improves work-life balance and accelerates your productivity.

Target Market(s)

ABC1

Industry/Entity Type

Business

Requirements
Must have
• Pictures/photos of garden office buildings and garden studios in typical UK garden surroundings. Contemporary structures essential with modern building design.
Nice to have
• Internal pictures of people working in a garden room or garden studio environment.

```html
<!DOCTYPE html>
<html lang="en">
<head>
<meta charset="utf-8">
<title>Corrick Yard Buildings – Leaflet Inside Spread</title>
<link rel="stylesheet" href="https://fonts.googleapis.com/css2?family=Source+Sans+3:wght@400;700&display=swap">
<style>
  :root {
    --page-bg: #ffffff;
    --frame: #222222;
    --text-green: #1b7a3c;
    --title-green: #3aad3a;
    --soft-mint: #eef8f1;
    --mint-edge: #dff0e4;
    --badge-mint: #a8dcb8;
    --bloom: #b9a9d8;
    --planter-wood: #8a6240;
    --grass-light: #8fb86a;
    --grass-deep: #4f7d35;
  }
  html, body {
    margin: 0;
    padding: 0;
    width: 1200px;
    height: 1000px;
    overflow: hidden;
    background: var(--page-bg);
  }
  .spread {
    position: relative;
    width: 1200px;
    height: 1000px;
    font-family: "Source Sans 3", "Myriad Pro", sans-serif;
    color: var(--text-green);
  }
  .trim-frame {
    position: absolute;
    left: 0;
    top: 77px;
    width: 1198px;
    height: 850px;
    border: 1px solid var(--frame);
  }
  .service-intro {
    position: absolute;
    left: 20px;
    top: 193px;
    width: 370px;
    margin: 0;
    font-size: 22px;
    line-height: 28.7px;
    text-align: center;
    white-space: nowrap;
  }
  .consult-disc {
    position: absolute;
    left: 450px;
    top: 182px;
    width: 300px;
    height: 292px;
    border-radius: 50%;
    background: var(--soft-mint);
    border: 1px solid var(--mint-edge);
  }
  .consult-note {
    position: absolute;
    left: 430px;
    top: 277px;
    width: 340px;
    margin: 0;
    font-size: 22px;
    line-height: 29px;
    text-align: center;
    white-space: nowrap;
  }
  .brand-name {
    position: absolute;
    left: 795px;
    top: 122px;
    width: 390px;
    margin: 0;
    font-size: 76px;
    font-weight: 700;
    line-height: 112px;
    color: var(--title-green);
    text-align: center;
  }
  .brand-dot {
    position: absolute;
    left: 1103px;
    top: 232px;
    width: 64px;
    height: 64px;
    border-radius: 50%;
    background: var(--badge-mint);
  }
  .garden-scene {
    position: absolute;
  }
  .garden-scene--wide {
    left: 20px;
    top: 585px;
    width: 773px;
    height: 323px;
    background: linear-gradient(180deg, #e4ddef 0%, var(--bloom) 25%, var(--planter-wood) 48%, var(--grass-light) 70%, var(--grass-deep) 100%);
  }
  .garden-scene--tall {
    left: 795px;
    top: 468px;
    width: 390px;
    height: 440px;
    background: linear-gradient(180deg, #e6e8ec 0%, #c9ccd6 22%, var(--bloom) 42%, var(--planter-wood) 70%, #5e4430 100%);
  }
</style>
</head>
<body>
  <main class="spread">
    <div class="trim-frame"></div>

    <p class="service-intro">Corrick Yard Buildings offer a<br>bespoke garden room building<br>service from design, construction,<br>installation and maintenance.-<br>Typical uses are for home office,<br>garden studio, playrooms, garage<br>workshops, therapy rooms and<br>extra living accommodation.<br>Including connection to all<br>services as required.</p>

    <div class="consult-disc"></div>
    <p class="consult-note">Contact us for a no obligation<br>consultation to see how we can<br>make your vision become a<br>reality.</p>

    <h1 class="brand-name">Corrick<br>Yard<br>Buildings</h1>
    <div class="brand-dot"></div>

    <div class="garden-scene garden-scene--wide" role="img" aria-label="Garden scene: gardeners with a wheelbarrow among wooden raised planters of purple and yellow flowers on a lawn"></div>
    <div class="garden-scene garden-scene--tall" role="img" aria-label="Garden scene: a gardener holding a rake and another carrying a flower pot beside wooden planters and climbing plants"></div>
  </main>
</body>
</html>
```